Cover needed for Sonqueue/plavio/digital release

Cover design needed for a Reggae song to be released as a single on sonqueue/ disc nest/ plavio/ vidarama etc... for the artist it should say Marcus Velden Meets Bluvaros and the song: Step and Sway Out. At the top it should say Marcus Velden and (Meets Bluvaros) can be in smaller letters. and the song title towards the bottom. Plus I would also like the same cover done without (Meets Bluvaros) included in the picture. So in total 2 images. The image theme can be reggae/ dancehall/ rub a dub/ vinyl turntable related. Here is some information about the image quality that the website I am using wants it in:
1400 x 1400 pixels minimum; 3000 x 3000 pixels maximum
PNG, GIF, JPG, or JPEG file type
72 - 300dpi (300dpi is the best)
Less than 25mb
RGB color scheme (not CMYK)
Unique to this particular title. We cannot accept artwork that has been used for another title.
Uploaded image must match your physical album cover artwork.
IMPORTANT: If your artist name and the title of your album or single appear on your cover artwork, it MUST precisely match the information you provided for this project. The text should be identical. For instance, if the artist name you provided is "Perry & Lindqvist (featuring Moss & Tarrant)," the text on your artwork should NOT say "Perry and Lindqvist."
Updates
I upgraded to be able to choose from more designs. Thank You
Target Market(s)
target market: Just Reggae fans dub fans, rub a dub/dancehall fans,

```html
<!DOCTYPE html>
<html lang="en">
<head>
<meta charset="utf-8">
<title>Marcus Velden Meets Bluvaros – Step and Sway Out</title>
<link rel="stylesheet" href="https://fonts.googleapis.com/css2?family=Archivo+Black&family=Anton&family=Oswald:wght@500&display=swap">
<style>
  :root {
    --sky-deep: #5e0a1e;
    --sky-mid: #b3123f;
    --sky-glow: #f0418a;
    --sky-light: #f6a3c8;
    --silhouette: #1a0508;
    --ink: #000000;
    --paper: #ffffff;
  }
  html, body {
    margin: 0;
    padding: 0;
    width: 1200px;
    height: 1200px;
    overflow: hidden;
    background: var(--sky-deep);
  }
  .cover {
    display: block;
    width: 1200px;
    height: 1200px;
  }
  .artist-name {
    font-family: "Anton", "Archivo Black", sans-serif;
    font-size: 92px;
  }
  .artist-feature {
    font-family: "Oswald", sans-serif;
    font-weight: 500;
    font-size: 46px;
  }
  .title-word {
    font-family: "Archivo Black", sans-serif;
  }
  .outlined {
    fill: var(--paper);
    stroke: var(--ink);
    stroke-linejoin: round;
    paint-order: stroke fill;
  }
</style>
</head>
<body>
<svg class="cover" viewBox="0 0 1200 1200" xmlns="http://www.w3.org/2000/svg">
  <defs>
    <radialGradient id="sunburst" cx="0.55" cy="0.6" r="0.75">
      <stop offset="0" stop-color="var(--sky-light)"/>
      <stop offset="0.35" stop-color="var(--sky-glow)"/>
      <stop offset="0.75" stop-color="var(--sky-mid)"/>
      <stop offset="1" stop-color="var(--sky-deep)"/>
    </radialGradient>
    <linearGradient id="crowd-shade" x1="0" y1="0" x2="0" y2="1">
      <stop offset="0" stop-color="var(--silhouette)" stop-opacity="0"/>
      <stop offset="1" stop-color="var(--silhouette)" stop-opacity="0.9"/>
    </linearGradient>
    <linearGradient id="palm-shade-left" x1="0" y1="0" x2="1" y2="0">
      <stop offset="0" stop-color="var(--silhouette)" stop-opacity="0.85"/>
      <stop offset="1" stop-color="var(--silhouette)" stop-opacity="0"/>
    </linearGradient>
  </defs>

  <g class="backdrop" role="img" aria-label="Palm tree silhouettes framing a pink sunburst sky over a cheering crowd with raised hands and sound level bars">
    <rect width="1200" height="1200" fill="url(#sunburst)"/>
    <rect width="420" height="1200" fill="url(#palm-shade-left)"/>
    <rect y="980" width="1200" height="220" fill="url(#crowd-shade)"/>
  </g>

  <g class="artist-block" text-anchor="middle">
    <text class="artist-name outlined" x="600" y="186" textLength="400" lengthAdjust="spacingAndGlyphs" stroke-width="22">Marcus Velden</text>
    <text class="artist-feature outlined" x="600" y="236" textLength="340" lengthAdjust="spacing" stroke-width="16">Meets Bluvaros</text>
  </g>

  <g class="song-title" text-anchor="middle">
    <text class="title-word outlined" x="598" y="664" font-size="340" textLength="772" lengthAdjust="spacingAndGlyphs" stroke-width="30">Step</text>
    <text class="title-word outlined" x="604" y="960" font-size="290" textLength="1064" lengthAdjust="spacingAndGlyphs" stroke-width="28">Sway Out</text>
    <text class="title-word outlined" x="595" y="742" font-size="80" textLength="150" lengthAdjust="spacingAndGlyphs" stroke-width="12">and</text>
  </g>
</svg>
</body>
</html>
```